Billboard for personal injury chiropractors office

We are a personal injury chiropractor clinic.
I need a Billboard with the company name as the dominating factor. Also a smaller picture or 2 of something creative, like a car accident or an arm in a cast off to the sides.
We Like something Clean and Simple and Eye Catching. Please make the picture Small and Off To The Side. The MAIN FOCUS areas are the… name Pell Chiropractic Clinic
At the top CAR ACCIDENT INJURY?
AND at the bottom our number 581-47-TORSO.
Dr.Marla T. Pell in bold somewhere with the word chiropractor under the doctors name in a text.

Im open to red lettering on white backgrounds, red on yellow backgrounds and I'm also open to reds blues white and yellow. I'd prefer yellow if used be across the bottom.

I am uploading a very rough draft of what we are after along with a screenshot of the tv commercial showing the yellow

DO NOT USE THE LOGO ON THE COMMERCIAL. I JUST WANT THE NAME TYPED LIKE ON SAMPLE BILLBOARD.

Industry/Entity Type

Chiropractic

Colors
0054AA
0677BA
7BADD7
CADEEF
E8F1F8
FFF300
FFF600
FEFA6F
FFFEC7
FFFEE8
EB3D1F
EC4F4E
F09395
F8D3D4
FCEDEE

Requirements
Must have
• Eye catching ,bold

```html
<!DOCTYPE html>
<html lang="en">
<head>
<meta charset="utf-8">
<title>Pell Chiropractic Clinic — Billboard</title>
<link rel="stylesheet" href="https://fonts.googleapis.com/css2?family=Oswald:wght@600;700&family=Nunito:wght@800&family=Audiowide&display=swap">
<style>
  :root {
    --red: #EB3D1F;
    --red-deep: #D12A22;
    --yellow: #FFF300;
    --yellow-soft: #FFFEC7;
    --blue: #0054AA;
    --blue-mid: #0677BA;
    --white: #FFFFFF;
    --photo-light: #9a9a9a;
    --photo-dark: #3c3c3c;
    --cast-dark: #1d1d1f;
  }
  html, body {
    margin: 0;
    padding: 0;
    width: 1044px;
    height: 1200px;
    overflow: hidden;
    background: var(--white);
  }
  .billboard {
    position: absolute;
    left: 22px;
    top: 454px;
    width: 1000px;
    height: 292px;
    display: block;
  }
  .headline {
    font-family: "Oswald", "Arial Narrow", sans-serif;
    font-weight: 700;
    font-size: 60px;
    fill: var(--red-deep);
    stroke: var(--yellow);
    stroke-width: 3px;
    paint-order: stroke;
  }
  .clinic-name {
    font-family: "Oswald", "Arial Narrow", sans-serif;
    font-weight: 700;
    font-size: 47px;
    fill: var(--red-deep);
  }
  .clinic-word {
    font-family: "Oswald", "Arial Narrow", sans-serif;
    font-weight: 700;
    font-size: 26px;
    letter-spacing: 7px;
    fill: var(--blue);
  }
  .call-label {
    font-family: "Nunito", "Arial Rounded MT Bold", sans-serif;
    font-weight: 800;
    font-size: 30px;
    fill: var(--blue);
  }
  .phone {
    font-family: "Audiowide", "Arial Black", sans-serif;
    font-size: 40px;
    fill: var(--white);
    stroke: var(--blue);
    stroke-width: 3px;
    paint-order: stroke;
  }
  .doctor-name {
    font-family: "Oswald", "Arial Narrow", sans-serif;
    font-weight: 700;
    font-size: 21px;
    fill: var(--white);
  }
  .doctor-title {
    font-family: "Oswald", "Arial Narrow", sans-serif;
    font-weight: 600;
    font-size: 11px;
    fill: var(--white);
  }
</style>
</head>
<body>
<svg class="billboard" viewBox="0 0 886 258" xmlns="http://www.w3.org/2000/svg" aria-label="Pell Chiropractic Clinic billboard">
  <defs>
    <linearGradient id="headline-band" x1="0" y1="0" x2="1" y2="0">
      <stop offset="0" stop-color="var(--white)"/>
      <stop offset="0.35" stop-color="var(--yellow-soft)"/>
      <stop offset="0.7" stop-color="var(--yellow)"/>
    </linearGradient>
    <linearGradient id="crash-photo" x1="0" y1="0" x2="1" y2="1">
      <stop offset="0" stop-color="var(--photo-light)"/>
      <stop offset="0.6" stop-color="#6a6a6a"/>
      <stop offset="1" stop-color="var(--photo-dark)"/>
    </linearGradient>
    <linearGradient id="cast-photo" x1="0" y1="0" x2="1" y2="1">
      <stop offset="0" stop-color="var(--cast-dark)"/>
      <stop offset="0.45" stop-color="#1f6fd0"/>
      <stop offset="0.8" stop-color="#2a2a2c"/>
      <stop offset="1" stop-color="var(--cast-dark)"/>
    </linearGradient>
  </defs>

  <rect class="backdrop" x="0" y="0" width="886" height="258" fill="var(--white)"/>

  <polygon class="headline-band" points="185,0 748,0 728,76 185,76" fill="url(#headline-band)"/>

  <path class="crash-photo" role="img" aria-label="Photo of a damaged car with a young man on the phone beside it"
        d="M0 0 H246 C205 60 178 140 166 258 H0 Z" fill="url(#crash-photo)"/>

  <path class="number-band" d="M166 258 C176 226 196 200 232 184 H697 V258 Z" fill="var(--yellow)"/>

  <rect class="cast-photo" role="img" aria-label="Photo of an arm in a blue cast being held" x="717" y="0" width="169" height="182" fill="url(#cast-photo)"/>

  <rect class="doctor-panel" x="708" y="184" width="178" height="74" fill="var(--blue)"/>

  <text class="headline" x="454" y="69" text-anchor="middle">CAR ACCIDENT INJURY?</text>
  <text class="clinic-name" x="455" y="141" text-anchor="middle">PELL CHIROPRACTIC</text>
  <text class="clinic-word" x="458" y="171" text-anchor="middle">CLINIC</text>

  <text class="call-label" x="232" y="230">call us :</text>
  <text class="phone" x="381" y="237" textLength="298" lengthAdjust="spacingAndGlyphs">581 47 TORSO</text>

  <text class="doctor-name" x="797" y="221" text-anchor="middle">Dr.Marla T. Pell</text>
  <text class="doctor-title" x="797" y="236" text-anchor="middle">chiropractor</text>
</svg>
</body>
</html>
```